Banner Designs for Trek Haven Ad Campaign

Quorvane is a security consulting and services company that offers a service called TrekHaven. TrekHaven helps our customers secure large events by providing rapidly deployable security and communications technologies in a Trek Haven vehicle, on a per event basis. We are looking for a designer to create a banner ad in three sizes for our campaign.
Target Market(s)
Our campaign is geared to the sports and entertainment industry, specifically large event venues and their security operation.
Industry/Entity Type
Security
Font styles to use
Other font styles liked:
- Raleway
Requirements
Must have
- Banner Objective
The visual and textual content of the banner should prompt the viewer to quickly identify the service offered and the information that is available to download.
Banner Design
Logo: TrekHaven logo
Call to Action Button in Red: Get Details (On Right or or Upper Right)
Title in Larger Font: Take Control of you Events
Subtitle in smaller Font: Your Force Multiplier - Trek Haven as a Service
Background: Photo of Trek Haven interior or exterior or photo of female operator.
Font: Raleway
Banner Sizes
1 - 1200x670 pixels
2 - 1510x196 pixels
3 - 1200x628 pixels
Nice to have
- Follow the look and feel of the samples provided.

```html
<!DOCTYPE html>
<html lang="en">
<head>
<meta charset="utf-8">
<title>TrekHaven Banner Set</title>
<link rel="stylesheet" href="https://fonts.googleapis.com/css2?family=Raleway:wght@400;500;700;800;900&display=swap">
<style>
  :root {
    --ink: #05060f;
    --brand-blue: #3179bf;
    --white: #ffffff;
    --grey: #c9ccd3;
    --page: #ffffff;
    --photo-dark: #0d1a33;
    --photo-mid: #2a4a78;
    --photo-light: #7a8aa3;
  }
  * { margin: 0; padding: 0; box-sizing: border-box; }
  html, body { width: 857px; height: 1200px; overflow: hidden; background: var(--page); }
  body { position: relative; font-family: "Raleway", sans-serif; }

  .banner {
    position: absolute;
    left: 78px;
    width: 710px;
    background: var(--ink);
    overflow: hidden;
    box-shadow: 12px 14px 22px rgba(0,0,0,0.45);
  }
  .banner--large { top: 51px; height: 394px; }
  .banner--strip { top: 539px; height: 121px; }
  .banner--medium { top: 755px; height: 371px; }

  .banner__art { position: absolute; inset: 0; width: 100%; height: 100%; }

  .brand { position: absolute; color: var(--white); line-height: 1; }
  .brand__name { display: flex; align-items: center; gap: 6px; font-weight: 500; }
  .brand__dot { width: 10px; height: 10px; border-radius: 50%; background: var(--brand-blue); }
  .brand__by { font-weight: 500; text-align: right; color: var(--grey); margin-top: 4px; }

  .headline { position: absolute; color: var(--brand-blue); line-height: 0.98; letter-spacing: -0.5px; }
  .headline__top { display: block; font-weight: 700; }
  .headline__bottom { display: block; font-weight: 900; }

  .subline { position: absolute; color: var(--white); font-weight: 500; line-height: 1.3; }

  .cta {
    position: absolute;
    background: var(--brand-blue);
    color: var(--white);
    font-weight: 700;
    border-radius: 30px;
    display: flex; align-items: center; justify-content: center;
  }

  /* Large banner */
  .banner--large .brand { left: 18px; top: 26px; }
  .banner--large .brand__name { font-size: 24px; }
  .banner--large .brand__by { font-size: 11px; }
  .banner--large .headline { left: 19px; top: 126px; font-size: 45px; }
  .banner--large .subline { left: 20px; top: 236px; font-size: 25px; }
  .banner--large .cta { left: 16px; top: 330px; width: 222px; height: 48px; font-size: 32px; }

  /* Strip banner */
  .banner--strip .brand { left: 6px; top: 44px; }
  .banner--strip .brand__name { font-size: 15px; }
  .banner--strip .brand__dot { width: 7px; height: 7px; }
  .banner--strip .brand__by { font-size: 7px; }
  .banner--strip .headline { left: 170px; width: 230px; top: 12px; font-size: 26px; text-align: center; }
  .banner--strip .subline { left: 170px; width: 230px; top: 74px; font-size: 14px; text-align: center; line-height: 1.3; }
  .banner--strip .corner-cta {
    position: absolute; right: -4px; top: 22px;
    transform: rotate(45deg);
    color: var(--white); font-weight: 700; font-size: 13px; line-height: 1.05; text-align: center;
  }

  /* Medium banner */
  .banner--medium .brand { left: 20px; top: 26px; }
  .banner--medium .brand__name { font-size: 24px; }
  .banner--medium .brand__by { font-size: 11px; }
  .banner--medium .headline { left: 15px; top: 110px; font-size: 44px; }
  .banner--medium .subline { left: 13px; top: 208px; font-size: 25px; }
  .banner--medium .cta { left: 20px; top: 302px; width: 208px; height: 48px; font-size: 32px; }
</style>
</head>
<body>

<section class="banner banner--large">
  <svg class="banner__art" viewBox="0 0 1345 746" preserveAspectRatio="none">
    <defs>
      <linearGradient id="photoLarge" x1="0" y1="0" x2="1" y2="1">
        <stop offset="0" stop-color="#2a4a78"/>
        <stop offset="0.5" stop-color="#0d1a33"/>
        <stop offset="1" stop-color="#7a8aa3"/>
      </linearGradient>
    </defs>
    <polygon role="img" aria-label="Photo of a female operator with headset in a security control room" points="597,0 1345,0 1345,746 1042,746" fill="url(#photoLarge)"/>
    <polygon points="824,381 897,381 1140,746 1042,746" fill="#3179bf"/>
  </svg>
  <div class="brand">
    <div class="brand__name"><span class="brand__dot"></span>TrekHaven</div>
    <div class="brand__by">By Quorvane</div>
  </div>
  <h1 class="headline"><span class="headline__top">TAKE CONTROL</span><span class="headline__bottom">OF YOU EVENTS</span></h1>
  <p class="subline">Your Force Multiplier -<br>Trek Haven as a Service</p>
  <a class="cta">Get Details</a>
</section>

<section class="banner banner--strip">
  <svg class="banner__art" viewBox="0 0 1345 229" preserveAspectRatio="none">
    <defs>
      <linearGradient id="photoStrip" x1="0" y1="0" x2="1" y2="1">
        <stop offset="0" stop-color="#2a4a78"/>
        <stop offset="0.5" stop-color="#0d1a33"/>
        <stop offset="1" stop-color="#7a8aa3"/>
      </linearGradient>
    </defs>
    <polygon role="img" aria-label="Photo of a female operator with headset in a security control room" points="772,0 1345,0 1345,229 967,229" fill="url(#photoStrip)"/>
    <polygon points="861,102 935,102 1040,229 967,229" fill="#3179bf"/>
    <polygon points="1217,0 1345,0 1345,165" fill="#3179bf"/>
  </svg>
  <div class="brand">
    <div class="brand__name"><span class="brand__dot"></span>TrekHaven</div>
    <div class="brand__by">By Quorvane</div>
  </div>
  <h2 class="headline"><span class="headline__top">TAKE CONTROL</span><span class="headline__bottom">OF YOU EVENTS</span></h2>
  <p class="subline">Your Force Multiplier -<br>Trek Haven as a Service</p>
  <a class="corner-cta">Get<br>Details</a>
</section>

<section class="banner banner--medium">
  <svg class="banner__art" viewBox="0 0 1345 703" preserveAspectRatio="none">
    <defs>
      <linearGradient id="photoMedium" x1="0" y1="0" x2="1" y2="1">
        <stop offset="0" stop-color="#2a4a78"/>
        <stop offset="0.5" stop-color="#0d1a33"/>
        <stop offset="1" stop-color="#7a8aa3"/>
      </linearGradient>
    </defs>
    <polygon role="img" aria-label="Photo of a female operator with headset in a security control room" points="592,0 1345,0 1345,703 1012,703" fill="url(#photoMedium)"/>
    <polygon points="798,345 880,345 1100,703 1012,703" fill="#3179bf"/>
  </svg>
  <div class="brand">
    <div class="brand__name"><span class="brand__dot"></span>TrekHaven</div>
    <div class="brand__by">By Quorvane</div>
  </div>
  <h2 class="headline"><span class="headline__top">TAKE CONTROL</span><span class="headline__bottom">OF YOU EVENTS</span></h2>
  <p class="subline">Your Force Multiplier -<br>Trek Haven as a Service</p>
  <a class="cta">Get Details</a>
</section>

</body>
</html>
```